Investor Information Presentation Design Required and Corporate overview design

I have all the materials ready to go, just need 1x Pro Design for the presentation and 1x Pro Design for the corporate overview.
I am ok with images being changed (only if it represents the company better). Wording Can NOT be changed. Any process diagrams can be changed to better represent the process.
I can provide high res Logo file and obviously the files for the presentation and corporate overview. What I have done is basic, but need it to look far more polished and professional.

Target Market(s)

Fixed Term Deposits - $100,000 + High interest rates

Industry/Entity Type

Investment

Font styles to use
Sans Serif

Requirements
Must have
• A corporate professional look, think banks, financial services, business etc
• The presentation is NOT used for group presenting purposes - Individuals go through it on their own. Should want to make me feel like I have to read it all!

```html
<!DOCTYPE html>
<html lang="en">
<head>
<meta charset="utf-8">
<title>Investor Presentation – Slide Set</title>
<link href="https://fonts.googleapis.com/css2?family=Roboto:wght@300;400;500;700&display=swap" rel="stylesheet">
<style>
:root{
  --page:#e9eaec;
  --navy:#1d4877;
  --navy-deep:#193e68;
  --sky:#29a3e0;
  --grey:#85888d;
  --ring-grey:#b5b7ba;
  --ink:#333;
  --white:#fff;
}
*{box-sizing:border-box;margin:0;padding:0}
html,body{width:1200px;height:900px;overflow:hidden;background:var(--page);font-family:'Roboto',Arial,sans-serif;color:var(--ink)}
.canvas{position:relative;width:1200px;height:900px}
.set-label{position:absolute;left:110px;top:71px;font-size:9px;color:var(--sky);letter-spacing:.2px}
.slide{position:absolute;width:325px;height:182px;background:var(--white);overflow:hidden}
.c1{left:110px}.c2{left:440px}.c3{left:772px}
.r1{top:88px}.r2{top:278px}.r3{top:467px}.r4{top:657px}
.slide-title{position:absolute;left:13px;top:12px;font-size:8.5px;font-weight:300;color:var(--sky);text-transform:uppercase}
.slide-title span{border-bottom:1px solid var(--navy)}
.brand{position:absolute;right:8px;top:8px;display:flex;flex-direction:column;align-items:center;gap:1px}
.brand i{display:block;width:8px;height:8px;background:var(--navy);border-radius:50%}
.brand b{font-weight:400;font-size:3.4px;color:var(--navy);white-space:nowrap}
.footer{position:absolute;left:0;right:0;bottom:0;height:5px;background:var(--navy);font-size:2.6px;color:var(--white);padding-left:5px;line-height:5px}
.footer em{position:absolute;right:0;top:0;width:20px;height:5px;background:var(--sky);font-style:normal;text-align:center}
.tiny{font-size:3.2px;line-height:1.55;color:var(--ink);text-align:justify}
.tiny h4{font-size:3.2px;color:var(--sky);font-weight:500}
.tiny strong{font-weight:700}
.photo{position:absolute}
.vm-photo{left:0;top:0;width:325px;height:100px;background:linear-gradient(135deg,#2d5c8e,#5d82ad 60%,#456f9e)}
.vm-band{position:absolute;left:0;top:100px;width:325px;height:82px;background:var(--grey)}
.vm-icon{position:absolute;top:78px;width:37px;height:37px;border-radius:50%;background:var(--sky);border:2px solid var(--white);display:flex;align-items:center;justify-content:center}
.vm-text{position:absolute;top:122px;width:110px;font-size:4.6px;line-height:1.5;color:var(--white);text-align:center}
.donut{position:absolute;top:60px;width:52px;height:52px}
.donut-cap{position:absolute;top:116px;width:72px;font-size:3px;line-height:1.45;text-align:center;color:#555}
.svc{position:absolute;top:47px;width:64px}
.svc-head{height:42px;background:var(--navy);color:var(--white);font-size:4.5px;font-weight:500;text-align:center;padding-top:5px}
.svc.light .svc-head{background:var(--sky)}
.svc-head svg{display:block;margin:0 auto 3px}
.svc-body{height:58px;margin-top:2px;background:var(--sky);color:var(--white);font-size:3.1px;line-height:1.5;text-align:center;padding:8px 5px}
.ring{position:absolute;top:66px;width:60px;height:60px;border-radius:50%;display:flex;align-items:center;justify-content:center}
.ring.blue{background:var(--sky)}
.ring.grey{background:var(--ring-grey)}
.ring span{width:38px;height:38px;border-radius:50%;border:2px solid var(--white);background:var(--navy);display:flex;align-items:center;justify-content:center}
.ring.grey span{background:var(--grey)}
.ring.blue.light span{background:var(--sky)}
.cap{position:absolute;font-size:3px;line-height:1.45;width:58px;color:#333}
.p-node{position:absolute;width:17px;height:17px;border-radius:50%;border:1.4px solid var(--grey);background:var(--white);display:flex;align-items:center;justify-content:center}
.p-node.sky{border-color:var(--sky)}
.p-label{position:absolute;font-size:2.6px;color:#555}
.it-panel{position:absolute;left:0;top:0;width:158px;height:182px;background:var(--navy)}
.it-photo{left:158px;top:0;width:167px;height:182px;background:linear-gradient(160deg,#d9dfe6,#a7b3c0 55%,#3a4656)}
.sec-photo{left:0;top:0;width:325px;height:182px;background:linear-gradient(135deg,#2a5584,#1c446f 60%,#264f7c)}
.map{left:0;top:72px;width:325px;height:82px;background:linear-gradient(160deg,#e3e4e0,#cfd2cc 50%,#b7c3cf)}
.contact{position:absolute;left:0;top:154px;width:325px;height:23px;background:var(--navy);display:flex;align-items:center;justify-content:space-around;font-size:4.2px;color:var(--white)}
.contact span{display:flex;align-items:center;gap:3px}
.contact-rule{position:absolute;left:0;bottom:0;width:325px;height:5px;background:var(--sky)}
</style>
</head>
<body>
<div class="canvas">
<p class="set-label">ADDITIONAL SLIDE</p>

<section class="slide c1 r1">
  <div class="photo vm-photo" role="img" aria-label="Desk with coffee cup and documents, tinted blue"></div>
  <h2 class="slide-title" style="color:#fff"><span style="border-color:#fff">Vision &amp; Mission</span></h2>
  <div class="vm-band"></div>
  <div class="vm-icon" style="left:68px"><svg width="18" height="12" viewBox="0 0 18 12" fill="none" stroke="#fff" stroke-width="1.6"><circle cx="5" cy="7" r="3.5"/><circle cx="13" cy="7" r="3.5"/><path d="M8.5 6h1"/></svg></div>
  <div class="vm-icon" style="left:203px"><svg width="18" height="14" viewBox="0 0 18 14" fill="none" stroke="#fff" stroke-width="1.6"><path d="M2 12a7 7 0 1 1 14 0"/><path d="M9 12l4-5"/></svg></div>
  <p class="vm-text" style="left:31px">To provide state of the art logistical and supply chain solutions to the defined needs of our customers using the best people, processes and systems in creating efficient and effective results.</p>
  <p class="vm-text" style="left:164px">To provide state of the art logistical and supply chain solutions to the defined needs of our customers using the best people, processes and systems in creating efficient and effective results.</p>
</section>

<section class="slide c2 r1">
  <h2 class="slide-title"><span>Title goes here</span></h2>
  <div class="brand"><i></i><b>Quillmere Capital</b></div>
  <div class="photo" style="left:15px;top:38px;width:74px;height:47px;background:linear-gradient(135deg,#c9d2dc,#3d4a5c)" role="img" aria-label="Business team reviewing documents"></div>
  <p class="tiny" style="position:absolute;left:15px;top:90px;width:74px;text-align:center;color:var(--sky);font-weight:500">LOREM IPSUM DOLOR SIT MET CONSECTUR ADIPISCING ELIT, SED DO EIUSMOD TEMPOR INCIDIDUNT UT LABORE ET DOLORE MAGNA</p>
  <div class="tiny" style="position:absolute;left:110px;top:38px;width:88px">
    <h4>Lorem ipsum dolor sit amet</h4>
    <p>Lorem ipsum dolor sit amet, consectetur adipiscing elit, sed do eiusmod tempor incididunt ut labore et dolore magna aliqua. Ut enim ad minim veniam, quis nostrud exercitation ullamco laboris nisi ut aliquip ex ea commodo consequat.</p>
    <p style="margin-top:4px">Lorem ipsum dolor sit amet, consectetur adipiscing elit, sed do eiusmod tempor incididunt ut labore et dolore magna aliqua. Ut enim ad minim veniam, quis nostrud exercitation ullamco.</p>
  </div>
  <div class="tiny" style="position:absolute;left:210px;top:38px;width:88px">
    <h4>Lorem ipsum dolor sit amet</h4>
    <p>Lorem ipsum dolor sit amet, consectetur adipiscing elit, sed do eiusmod tempor incididunt ut labore et dolore magna aliqua. Ut enim ad minim veniam, quis nostrud exercitation ullamco laboris nisi ut aliquip ex ea commodo consequat.</p>
    <p style="margin-top:4px">Lorem ipsum dolor sit amet, consectetur adipiscing elit, sed do eiusmod tempor incididunt ut labore et dolore magna aliqua. Ut enim ad minim veniam, quis nostrud exercitation ullamco.</p>
  </div>
  <div class="footer">Quillmere Capital Pty Ltd ACN: 000 000 000<em>02</em></div>
</section>

<section class="slide c3 r1">
  <h2 class="slide-title"><span>Title goes here</span></h2>
  <div class="brand"><i></i><b>Quillmere Capital</b></div>
  <div style="position:absolute;left:0;top:52px;width:106px;height:60px;background:var(--navy);color:#fff;font-size:3.3px;line-height:1.6;font-weight:700;padding:19px 8px 0 20px">LOREM IPSUM DOLOR SIT MET CONSECTUR ADIPISCING ELIT, SED DO EIUSMOD TEMPOR INCIDIDUNT UT LABORE ET DOLORE MAGNA</div>
  <div class="photo" style="left:106px;top:52px;width:219px;height:60px;background:linear-gradient(90deg,#4a6a8e,#c6cfd8 50%,#8b9aab)" role="img" aria-label="Row of business people at a meeting"></div>
  <p class="tiny" style="position:absolute;left:106px;top:122px;width:205px">Lorem ipsum dolor sit amet, consectetur adipiscing elit, sed do eiusmod tempor incididunt ut labore et dolore magna aliqua. Ut enim ad minim veniam, quis nostrud exercitation ullamco laboris nisi ut aliquip ex ea commodo consequat. Duis aute irure dolor.</p>
  <div class="footer">Quillmere Capital Pty Ltd ACN: 000 000 000<em>02</em></div>
</section>

<section class="slide c1 r2">
  <h2 class="slide-title"><span>Our Chart</span></h2>
  <div class="brand"><i></i><b>Quillmere Capital</b></div>
  <svg class="donut" style="left:40px" viewBox="0 0 52 52"><circle cx="26" cy="26" r="20" fill="none" stroke="var(--ring-grey)" stroke-width="4.5"/><circle cx="26" cy="26" r="20" fill="none" stroke="var(--sky)" stroke-width="4.5" stroke-dasharray="101.8 125.7" transform="rotate(-90 26 26)"/><path d="M26 6a20 20 0 0 1 12 4" fill="none" stroke="var(--navy)" stroke-width="4.5"/><text x="26" y="29" text-anchor="middle" font-size="8" font-weight="500" fill="var(--navy)">81%</text></svg>
  <svg class="donut" style="left:136px" viewBox="0 0 52 52"><circle cx="26" cy="26" r="20" fill="none" stroke="var(--ring-grey)" stroke-width="4.5"/><circle cx="26" cy="26" r="20" fill="none" stroke="var(--navy)" stroke-width="4.5" stroke-dasharray="90.5 125.7" transform="rotate(-90 26 26)"/><text x="26" y="29" text-anchor="middle" font-size="8" font-weight="500" fill="var(--navy)">72%</text></svg>
  <svg class="donut" style="left:227px" viewBox="0 0 52 52"><circle cx="26" cy="26" r="20" fill="none" stroke="var(--ring-grey)" stroke-width="4.5"/><circle cx="26" cy="26" r="20" fill="none" stroke="var(--navy)" stroke-width="4.5" stroke-dasharray="79.2 125.7" transform="rotate(-90 26 26)"/><path d="M26 6a20 20 0 0 0 -14 6" fill="none" stroke="var(--sky)" stroke-width="4.5"/><text x="26" y="29" text-anchor="middle" font-size="8" font-weight="500" fill="var(--navy)">63%</text></svg>
  <p class="donut-cap" style="left:30px">dolor sit amet, consectetur adipiscing elit, sed do eiusmod tempor incididunt ut labore et dolore magna aliqua, ut enim ad minim veniam nostrud.</p>
  <p class="donut-cap" style="left:126px">dolor sit amet, consectetur adipiscing elit, sed do eiusmod tempor incididunt ut labore et dolore magna aliqua, ut enim ad minim veniam nostrud.</p>
  <p class="donut-cap" style="left:217px">dolor sit amet, consectetur adipiscing elit, sed do eiusmod tempor incididunt ut labore et dolore magna aliqua, ut enim ad minim veniam nostrud.</p>
  <div class="footer">Quillmere Capital Pty Ltd ACN: 000 000 000<em>02</em></div>
</section>

<section class="slide c2 r2">
  <h2 class="slide-title"><span>Our Chart</span></h2>
  <div class="brand"><i></i><b>Quillmere Capital</b></div>
  <div class="tiny" style="position:absolute;left:28px;top:55px;width:142px">
    <p><strong>Lorem ipsum dolor sit amet</strong><br>consectetur adipiscing elit, sed do eiusmod tempor incididunt ut labore et dolore magna aliqua. Ut enim ad minim veniam, quis nostrud exercitation ullamco laboris nisi ut aliquip.</p>
    <p style="margin-top:5px"><strong>Lorem ipsum dolor sit amet</strong><br>consectetur adipiscing elit, sed do eiusmod tempor incididunt ut labore et dolore magna aliqua. Ut enim ad minim veniam, quis nostrud exercitation ullamco laboris nisi ut aliquip.</p>
    <p style="margin-top:5px"><strong>Lorem ipsum dolor sit amet</strong><br>Excepteur sint occaecat cupidatat non proident, sunt in culpa qui officia deserunt mollit anim id est laborum.</p>
  </div>
  <svg style="position:absolute;left:205px;top:34px" width="110" height="56" viewBox="0 0 110 56">
    <line x1="2" y1="0" x2="2" y2="50" stroke="#999" stroke-width=".4"/>
    <line x1="2" y1="50" x2="108" y2="50" stroke="#999" stroke-width=".4"/>
    <g><rect x="8" y="18" width="4" height="32" fill="var(--sky)"/><rect x="12" y="36" width="4" height="14" fill="var(--ring-grey)"/><rect x="16" y="30" width="4" height="20" fill="var(--navy)"/></g>
    <g><rect x="32" y="32" width="4" height="18" fill="var(--sky)"/><rect x="36" y="10" width="4" height="40" fill="var(--ring-grey)"/><rect x="40" y="26" width="4" height="24" fill="var(--navy)"/><rect x="35" y="3" width="6" height="4" fill="var(--ring-grey)"/></g>
    <g><rect x="58" y="14" width="4" height="36" fill="var(--sky)"/><rect x="62" y="36" width="4" height="14" fill="var(--ring-grey)"/><rect x="66" y="28" width="4" height="22" fill="var(--navy)"/><rect x="57" y="7" width="6" height="4" fill="var(--sky)"/></g>
    <g><rect x="84" y="24" width="4" height="26" fill="var(--sky)"/><rect x="88" y="30" width="4" height="20" fill="var(--ring-grey)"/><rect x="92" y="12" width="4" height="38" fill="var(--navy)"/><rect x="91" y="5" width="6" height="4" fill="var(--navy)"/></g>
    <g font-size="3" fill="#555" text-anchor="middle"><text x="14" y="55">2009</text><text x="38" y="55">2010</text><text x="64" y="55">2011</text><text x="90" y="55">2012</text></g>
  </svg>
  <div class="tiny" style="position:absolute;left:225px;top:97px;width:80px;font-size:2.8px">
    <p><span style="display:inline-block;width:3px;height:3px;background:var(--sky)"></span> <strong>LOREM IPSUM</strong><br>Lorem ipsum dolor sit amet consectetur adipiscing elit.</p>
    <p style="margin-top:7px"><span style="display:inline-block;width:3px;height:3px;background:var(--ring-grey)"></span> <strong>LOREM IPSUM</strong><br>Lorem ipsum dolor sit amet consectetur adipiscing elit.</p>
    <p style="margin-top:7px"><span style="display:inline-block;width:3px;height:3px;background:var(--navy)"></span> <strong>LOREM IPSUM</strong></p>
  </div>
  <div class="footer">Quillmere Capital Pty Ltd ACN: 000 000 000<em>02</em></div>
</section>

<section class="slide c3 r2">
  <h2 class="slide-title"><span>Title goes here</span></h2>
  <div class="brand"><i></i><b>Quillmere Capital</b></div>
  <div class="svc" style="left:21px"><div class="svc-head"><svg width="16" height="16" viewBox="0 0 16 16"><path d="M8 1l7 7-7 7-7-7z" fill="#fff"/></svg>MANAGEMENT<br>SOLUTIONS</div><div class="svc-body">Dolor sit amet, consectetur adipiscing elit, sed do eiusmod tempor incididunt ut labore et dolore magna aliqua.</div></div>
  <div class="svc light" style="left:93px"><div class="svc-head"><svg width="16" height="16" viewBox="0 0 16 16"><circle cx="8" cy="8" r="7" fill="none" stroke="#fff" stroke-width="1.2"/><rect x="7.3" y="7" width="1.4" height="5" fill="#fff"/><circle cx="8" cy="4.8" r=".9" fill="#fff"/></svg>INFORMATION<br>SOLUTIONS</div><div class="svc-body">Dolor sit amet, consectetur adipiscing elit, sed do eiusmod tempor incididunt ut labore et dolore magna aliqua.</div></div>
  <div class="svc" style="left:165px"><div class="svc-head"><svg width="16" height="16" viewBox="0 0 16 16" fill="none" stroke="#fff" stroke-width="1.3"><path d="M1 8l4-3 3 2 3-2 4 3-4 4-3-2-3 2z"/></svg>PROFESSIONAL<br>SERVICES</div><div class="svc-body">Dolor sit amet, consectetur adipiscing elit, sed do eiusmod tempor incididunt ut labore et dolore magna aliqua.</div></div>
  <div class="svc light" style="left:237px"><div class="svc-head"><svg width="16" height="16" viewBox="0 0 16 16" stroke="#fff" stroke-width="1" fill="#fff"><line x1="8" y1="8" x2="3" y2="3"/><line x1="8" y1="8" x2="13" y2="3"/><line x1="8" y1="8" x2="8" y2="14"/><circle cx="8" cy="8" r="2"/><circle cx="3" cy="3" r="1.4"/><circle cx="13" cy="3" r="1.4"/><circle cx="8" cy="14" r="1.4"/></svg>ORGANIZATIONAL<br>TRANSFORMATION</div><div class="svc-body">Dolor sit amet, consectetur adipiscing elit, sed do eiusmod tempor incididunt ut labore et dolore magna aliqua.</div></div>
  <div class="footer">Quillmere Capital Pty Ltd ACN: 000 000 000<em>02</em></div>
</section>

<section class="slide c1 r3">
  <h2 class="slide-title"><span>Title goes here</span></h2>
  <div class="brand"><i></i><b>Quillmere Capital</b></div>
  <p class="cap" style="left:86px;top:30px"><strong>Lorem ipsum dolor sit amet</strong><br>Ut enim ad minim veniam, quis nostrud exercitation ullamco laboris nisi ut aliquip.</p>
  <p class="cap" style="left:189px;top:30px"><strong>Lorem ipsum dolor sit amet</strong><br>Ut enim ad minim veniam, quis nostrud exercitation ullamco laboris nisi ut aliquip.</p>
  <div class="ring blue" style="left:29px"><span><svg width="14" height="16" viewBox="0 0 14 16" fill="none" stroke="#fff" stroke-width="1.2"><rect x="1" y="2" width="12" height="13" rx="1"/><path d="M4 9l2 2 4-4"/></svg></span></div>
  <div class="ring grey" style="left:83px"><span><svg width="14" height="14" viewBox="0 0 14 14" fill="#fff"><circle cx="5" cy="5" r="4"/><path d="M6 6l7 7-1 1-7-7z"/></svg></span></div>
  <div class="ring blue light" style="left:137px"><span><svg width="12" height="15" viewBox="0 0 12 15" fill="none" stroke="#fff" stroke-width="1.2"><rect x="1" y="1" width="10" height="13"/><path d="M3 5h6M3 8h6M3 11h6"/></svg></span></div>
  <div class="ring grey" style="left:191px"><span><svg width="16" height="14" viewBox="0 0 16 14" fill="none" stroke="#fff" stroke-width="1.2"><rect x="5" y="1" width="10" height="7"/><circle cx="3" cy="5" r="1.6"/><path d="M3 7v6M1 13h4"/></svg></span></div>
  <div class="ring blue" style="left:245px"><span><svg width="16" height="16" viewBox="0 0 16 16" fill="none" stroke="#fff" stroke-width="1.2"><path d="M3 2l3 3-2 2c1 2 3 4 5 5l2-2 3 3-2 2C7 14 2 9 1 4z"/><text x="9" y="7" font-size="5" fill="#fff" stroke="none">24</text></svg></span></div>
  <p class="cap" style="left:33px;top:131px"><strong>Lorem ipsum dolor sit amet</strong><br>Ut enim ad minim veniam, quis nostrud exercitation ullamco laboris nisi ut aliquip.</p>
  <p class="cap" style="left:141px;top:131px"><strong style="color:var(--sky)">Lorem ipsum dolor sit amet</strong><br>Ut enim ad minim veniam, quis nostrud exercitation ullamco laboris nisi ut aliquip.</p>
  <p class="cap" style="left:244px;top:131px"><strong>Lorem ipsum dolor sit amet</strong><br>Ut enim ad minim veniam, quis nostrud exercitation ullamco laboris nisi ut aliquip.</p>
  <div class="footer">Quillmere Capital Pty Ltd ACN: 000 000 000<em>02</em></div>
</section>

<section class="slide c2 r3">
  <h2 class="slide-title"><span>Title goes here</span></h2>
  <div class="brand"><i></i><b>Quillmere Capital</b></div>
  <svg style="position:absolute;left:36px;top:50px" width="70" height="110"><path d="M12 12h28v8M12 60v10h28v-8M12 100h28v-28" fill="none" stroke="#888" stroke-width=".5"/><path d="M40 20h30M40 60h30" fill="none" stroke="#888" stroke-width=".5"/></svg>
  <div class="p-node sky" style="left:37px;top:52px"><svg width="8" height="8" viewBox="0 0 8 8" fill="none" stroke="var(--sky)" stroke-width=".8"><rect x="1" y="1" width="6" height="6"/></svg></div>
  <div class="p-node" style="left:37px;top:92px"><svg width="9" height="6" viewBox="0 0 9 6" fill="none" stroke="#777" stroke-width=".8"><path d="M0 3l3-2 3 2 3-2"/></svg></div>
  <div class="p-node" style="left:37px;top:132px"><svg width="8" height="8" viewBox="0 0 8 8" fill="none" stroke="#777" stroke-width=".8"><rect x="1" y="1" width="6" height="6"/><path d="M2 3h4M2 5h4"/></svg></div>
  <div class="p-node" style="left:95px;top:70px"><svg width="7" height="7" viewBox="0 0 7 7" stroke="#777" stroke-width=".9"><path d="M1 1l5 5M6 1L1 6"/></svg></div>
  <div class="p-node sky" style="left:95px;top:110px"><svg width="8" height="8" viewBox="0 0 8 8" fill="none" stroke="var(--sky)" stroke-width=".8"><circle cx="4" cy="4" r="3"/></svg></div>
  <span class="p-label" style="left:56px;top:63px">PROCESS</span>
  <span class="p-label" style="left:78px;top:80px">TOOLS</span>
  <span class="p-label" style="left:56px;top:102px">CULTURE</span>
  <span class="p-label" style="left:78px;top:118px">KEY<br>PROCESS<br>DRIVERS</span>
  <span class="p-label" style="left:56px;top:140px">COLLATERAL</span>
  <div class="tiny" style="position:absolute;left:133px;top:55px;width:172px">
    <h4>Lorem ipsum dolor sit amet</h4>
    <p>consectetur adipiscing elit, sed do eiusmod tempor incididunt ut labore et dolore magna aliqua. Ut enim ad minim veniam, quis nostrud exercitation ullamco laboris nisi ut aliquip ex ea commodo consequat.</p>
    <h4 style="margin-top:5px">Lorem ipsum dolor sit amet</h4>
    <p>consectetur adipiscing elit, sed do eiusmod tempor incididunt ut labore et dolore magna aliqua. Ut enim ad minim veniam, quis nostrud exercitation ullamco laboris nisi ut aliquip.</p>
  </div>
  <div class="footer">Quillmere Capital Pty Ltd ACN: 000 000 000<em>02</em></div>
</section>

<section class="slide c3 r3">
  <div class="it-panel"></div>
  <div class="photo it-photo" role="img" aria-label="Two business people reviewing a document"></div>
  <h2 class="slide-title" style="color:#fff"><span style="border:0">Image Text</span></h2>
  <div class="tiny" style="position:absolute;left:19px;top:50px;width:130px;color:#fff;font-weight:500;line-height:1.75">
    <p>Lorem ipsum dolor sit amet, consectetur adipiscing elit, sed do eiusmod tempor incididunt ut labore et dolore magna aliqua. Ut enim ad minim veniam, quis nostrud exercitation ullamco laboris nisi ut aliquip ex ea commodo consequat. Duis aute irure dolor in reprehenderit.</p>
    <p style="margin-top:4px">Lorem ipsum dolor sit amet, consectetur adipiscing elit, sed do eiusmod tempor incididunt ut labore et dolore.</p>
  </div>
  <div style="position:absolute;left:6px;top:158px;width:24px;height:18px;background:#fff;display:flex;flex-direction:column;align-items:center;justify-content:center;gap:1px"><i style="display:block;width:6px;height:6px;border-radius:50%;background:var(--navy)"></i><b style="font-size:2.6px;font-weight:400;color:var(--navy);white-space:nowrap">Quillmere</b></div>
</section>

<section class="slide c1 r4">
  <div class="photo sec-photo" role="img" aria-label="Business person holding a briefcase, tinted blue"></div>
  <div style="position:absolute;left:143px;top:74px;width:34px;height:34px;border-radius:50%;background:#fff;display:flex;align-items:center;justify-content:center"><svg width="10" height="20" viewBox="0 0 10 20" fill="var(--navy)"><circle cx="6" cy="3" r="2.4"/><path d="M3 8h5l-2 9h3l-1 2H2l2-9H2z"/></svg></div>
  <div style="position:absolute;left:106px;top:117px;width:112px;height:1px;background:rgba(255,255,255,.6)"></div>
  <h2 style="position:absolute;left:0;width:325px;top:125px;text-align:center;font-size:12px;font-weight:300;color:#fff">SECTION TITLE</h2>
</section>

<section class="slide c2 r4">
  <div style="position:absolute;left:0;top:0;width:325px;height:2px;background:var(--navy)"></div>
  <div style="position:absolute;left:18px;top:24px;display:flex;flex-direction:column;align-items:flex-start;gap:4px">
    <i style="display:block;width:20px;height:20px;border-radius:50%;background:var(--navy)"></i>
    <b style="font-weight:400;font-size:7.5px;color:var(--navy);letter-spacing:.5px">Quillmere Capital</b>
  </div>
  <div class="photo map" role="img" aria-label="Street map showing office location"></div>
  <svg style="position:absolute;left:254px;top:80px" width="6" height="9" viewBox="0 0 6 9"><path d="M3 9L0.5 4a2.5 2.5 0 1 1 5 0z" fill="#d9342b"/></svg>
  <div class="contact">
    <span><svg width="6" height="6" viewBox="0 0 6 6" fill="#fff"><path d="M3 0l3 3H5v3H1V3H0z"/></svg>120 Harbour Lane Suite 400</span>
    <span><svg width="6" height="6" viewBox="0 0 6 6" fill="none" stroke="#fff" stroke-width=".7"><circle cx="3" cy="3" r="2.5"/><path d="M1.5 2.5l1.5 1 1.5-1"/></svg>hello@quillmere-cap.com</span>
    <span><svg width="6" height="6" viewBox="0 0 6 6" fill="none" stroke="#fff" stroke-width=".7"><circle cx="3" cy="3" r="2.5"/><path d="M.5 3h5M3 .5v5"/></svg>www.quillmere-cap.com</span>
  </div>
  <div class="contact-rule"></div>
</section>
</div>
</body>
</html>
```